Magazine Cover & Back, Course Overview

Please read this whole description and follow directions before proceeding. Please do not submit multiple designs that look similar. If you submit multiple designs that look similar you will be disqualified and receive a poor rating. A magazine design includes a cover and back. This is a single design and should be submitted as such. Do not submit one design for the front only, then a separate design for the back, then a third mock up. Submit all as a single design. I need a magazine cover and back. The size will be standard paper size, 8-1/2" x 11". It will be used for a course overview, a summary of a boating instruction course. I have attached examples and pictures that can be used. I have also attached required content. The final designs must NOT be AI files. Text must be editable with Adobe Acrobat DC.

Target Market(s)

Military & Government

Industry/Entity Type

Military & Government

Requirements
Must have
• See attached.
Nice to have
• See attached.
Should not have
• See attached.

```html
<!DOCTYPE html>
<html lang="en">
<head>
<meta charset="utf-8">
<title>Diver Support Vessel Training – Course Overview</title>
<link rel="stylesheet" href="https://fonts.googleapis.com/css2?family=Archivo+Black&family=Oswald:wght@500;700&family=Montserrat:wght@300;500;600;700&display=swap">
<style>
  :root{
    --backdrop:#56665a;
    --sky-top:#2f6fc6;
    --sky-low:#a9c6e8;
    --shore:#6e6b5f;
    --water-top:#3a6aa6;
    --water-deep:#1c4479;
    --gold:#d9bf2b;
    --white:#ffffff;
    --ink:#111111;
    --panel:rgba(236,240,248,0.82);
  }
  *{margin:0;padding:0;box-sizing:border-box}
  html,body{width:1200px;height:789px;overflow:hidden;background:var(--backdrop)}
  .spread{position:absolute;left:59px;top:44px;width:1082px;height:700px;display:flex;box-shadow:0 8px 24px rgba(0,0,0,.35)}
  .page{position:relative;width:541px;height:700px;overflow:hidden}
  .scene{position:absolute;inset:0;background:linear-gradient(180deg,var(--sky-top) 0%,#5a92d6 30%,var(--sky-low) 52%,var(--shore) 56%,#5c5a50 61%,var(--water-top) 63%,#2c5a95 80%,var(--water-deep) 100%)}

  /* back cover */
  .overview{position:absolute;left:140px;top:270px;width:300px;height:330px;background:var(--panel);border-radius:24px;padding:62px 30px 0 34px;font-family:Montserrat,sans-serif;color:var(--ink)}
  .overview p{font-weight:600;font-size:13px;line-height:1.3;margin-bottom:18px}
  .brand-row{display:flex;align-items:center;gap:14px;margin-top:30px}
  .mark{display:flex;align-items:center;gap:6px;font-family:Montserrat,sans-serif;font-weight:600;font-size:11px;line-height:1.25;color:var(--ink)}
  .mark .dot{width:34px;height:34px;border-radius:50%;background:#1b2a44;flex:none}
  .edition{margin-top:20px;text-align:center;font-weight:700;font-size:13px}

  /* front cover */
  .spine-band{position:absolute;left:0;top:0;width:44px;height:100%;background:var(--gold)}
  .title{position:absolute;left:66px;top:38px;font-family:"Archivo Black",sans-serif;font-size:66px;line-height:.88;color:var(--white);letter-spacing:1px}
  .title .accent{color:var(--gold)}
  .tagline{position:absolute;left:66px;top:318px;width:390px;border-top:1px solid var(--white);border-bottom:1px solid var(--white);padding:7px 0;font-family:Montserrat,sans-serif;font-weight:300;font-size:13px;letter-spacing:2.6px;line-height:1.3;color:var(--white);white-space:nowrap}
  .front-brands{position:absolute;left:66px;top:388px;display:flex;align-items:center;gap:14px}
  .front-brands .mark{color:var(--white);font-size:10px}
  .front-brands .mark-firm{max-width:120px}
  .helm-photo{position:absolute;left:360px;top:372px;width:158px;height:158px;border-radius:50%;border:8px solid var(--gold);background:radial-gradient(circle at 45% 45%,#c9ccd0,#7d8186 60%,#4b4f55)}
  .boat-photo{position:absolute;left:120px;top:455px;width:270px;height:72px;background:linear-gradient(180deg,#d8dadc,#9ea2a6);border-radius:6px 6px 40px 60px;opacity:.85}
  .credentials{position:absolute;right:26px;top:536px;text-align:right;font-family:Oswald,sans-serif;font-weight:700;line-height:1;text-transform:uppercase;color:var(--white)}
  .credentials .gold{color:var(--gold)}
  .credentials .l1{font-size:36px}
  .credentials .l2{font-size:60px}
  .credentials .l3{font-size:48px}
  .corner{position:absolute;right:0;top:0;width:120px;height:120px}
</style>
</head>
<body>
<main class="spread">
  <section class="page back-cover">
    <div class="scene" role="img" aria-label="Photo of a calm bay under blue sky with a wooded shoreline and floating barriers"></div>
    <div class="overview">
      <p>Custom made course for specific users, scenarios and vessels based on oic involvement, client feedback and after action reviews</p>
      <p>Focused on safety &amp; close-quarters maneuvering</p>
      <div class="brand-row">
        <span class="mark"><span class="dot"></span>Captain Reyes</span>
        <span class="mark">Harbor Line Marine Services, LLC</span>
      </div>
      <div class="edition">2023 Edition</div>
    </div>
  </section>

  <section class="page front-cover">
    <div class="scene" role="img" aria-label="Photo of a grey diver support vessel on open water with wooded hills behind"></div>
    <div class="boat-photo" role="img" aria-label="Diver support vessel underway"></div>
    <div class="spine-band"></div>
    <svg class="corner" viewBox="0 0 120 120">
      <polygon points="40,0 120,0 120,80" fill="var(--gold)"/>
      <text x="86" y="28" transform="rotate(45 86 28)" text-anchor="middle" font-family="Montserrat,sans-serif" font-weight="700" font-size="9" fill="#111">INCLUDES</text>
      <text x="92" y="40" transform="rotate(45 86 28)" text-anchor="middle" font-family="Montserrat,sans-serif" font-weight="700" font-size="9" fill="#111">USEFUL AIDS</text>
    </svg>
    <h1 class="title">DIVER<br>SUPPORT<br>VESSEL<br><span class="accent">TRAINING</span></h1>
    <p class="tagline">ASSISTING NAVY SAILORS BECOME<br>MORE PROFICIENT COXWAINS</p>
    <div class="front-brands">
      <span class="mark"><span class="dot"></span>Captain Reyes</span>
      <span class="mark mark-firm">Harbor Line Marine Services, LLC</span>
    </div>
    <div class="helm-photo" role="img" aria-label="Photo of the vessel's helm console with wheel and controls"></div>
    <div class="credentials">
      <div class="l1"><span class="gold">Taught by</span> reputable</div>
      <div class="l2 gold">USCG Licenced</div>
      <div class="l3">Boat Captains</div>
    </div>
  </section>
</main>
</body>
</html>
```